Tarrow Building Ventures needs a Business card design and logo

We Need a business card design and logo for a Building & Construction business based in Melbourne. We work in both the Domestic & Commercial sector. We specialize in all aspects of building including extensions, Renovations, and alterations. Construction Management, Project Management, And labour hire
Updates

Industry/Entity Type

Business

```html
<!DOCTYPE html>
<html lang="en">
<head>
<meta charset="utf-8">
<title>Tarrow Building Ventures – Business Card</title>
<link href="https://fonts.googleapis.com/css2?family=Roboto+Condensed:wght@300;700&display=swap" rel="stylesheet">
<style>
  :root {
    --card-bg: #ffffff;
    --frame: #4a4a4a;
    --ink: #3a3a3a;
    --taupe: #b59a80;
    --tab-text: #ffffff;
  }
  html, body {
    margin: 0;
    padding: 0;
    width: 1200px;
    height: 749px;
    overflow: hidden;
    background: var(--card-bg);
  }
  .card {
    position: relative;
    width: 1200px;
    height: 749px;
    box-sizing: border-box;
    border: 1.5px solid var(--frame);
    background: var(--card-bg);
    font-family: "Roboto Condensed", "Arial Narrow", sans-serif;
    font-weight: 300;
    color: var(--ink);
  }
  .brand-mark {
    position: absolute;
    left: 128px;
    top: 60px;
  }
  .company-name {
    position: absolute;
    left: 72px;
    top: 218px;
    margin: 0;
    font-size: 49px;
    font-weight: 300;
    line-height: 1;
    letter-spacing: 0.2px;
  }
  .tagline {
    position: absolute;
    left: 72px;
    top: 286px;
    margin: 0;
    font-size: 29px;
    line-height: 1;
  }
  .contact-person {
    position: absolute;
    left: 889px;
    top: 64px;
    margin: 0;
    font-size: 37px;
    line-height: 1;
  }
  .services {
    position: absolute;
    left: 889px;
    top: 273px;
    right: 0;
    margin: 0;
    padding: 0;
    list-style: none;
  }
  .service {
    height: 55px;
    margin-bottom: 6px;
    padding-left: 28px;
    background: var(--taupe);
    color: var(--tab-text);
    font-weight: 700;
    font-size: 37px;
    line-height: 55px;
  }
  .contact-lines {
    position: absolute;
    left: 420px;
    top: 628px;
    margin: 0;
    font-style: normal;
    font-size: 37px;
    line-height: 51px;
  }
</style>
</head>
<body>
  <main class="card">
    <svg class="brand-mark" width="130" height="130" viewBox="0 0 130 130" aria-hidden="true">
      <circle cx="65" cy="65" r="60" fill="var(--taupe)"/>
    </svg>
    <h1 class="company-name">Tarrow Building Ventures</h1>
    <p class="tagline">Domestic &amp; Commercial Builders</p>

    <p class="contact-person">Marcus Hale</p>

    <ul class="services">
      <li class="service">- Extentions</li>
      <li class="service">- Renovations</li>
      <li class="service">- Alterations</li>
      <li class="service">- Decks</li>
      <li class="service">- Pargolas</li>
    </ul>

    <address class="contact-lines">
      Mobile: 0400 318 527&nbsp; / Office: (03) 9000 41732<br>
      Email: info@tarrow buildingventures.com
    </address>
  </main>
</body>
</html>
```